Weightloss company needs Business Card

We want a business card that is clean and professional, yet portrays that we are a friendly, innovative, and versatile program designed to fit the needs of our clients.
I would like there to be 2 sides, one side having an appointment card, and the other side containing the logo and business information. There can be decorations on both sides. The logo is attached.

Target Market(s)

Men and women 40-60

Industry/Entity Type

Business

Contact Information for Business Card

Font styles to use
Sans Serif

Requirements
Must have
• The logo, space for business information
Nice to have
• The colors in the logo
Should not have
• No pictures of people or food

```html
<!DOCTYPE html>
<html lang="en">
<head>
<meta charset="utf-8">
<title>Brightpath Weightloss – Business Card</title>
<link href="https://fonts.googleapis.com/css2?family=Lato:wght@400;700;900&display=swap" rel="stylesheet">
<style>
  :root {
    --backdrop: #5a5a5c;
    --card-white: #ffffff;
    --panel-mist: #f4f6f9;
    --brand-red: #e31e35;
    --sky-blue: #4dc0e8;
    --sky-light: #a8dcf4;
    --sky-pale: #d7eefa;
    --ink-black: #0c0c0c;
    --steel-gray: #7e8083;
    --ash-gray: #a9abae;
    --field-1: #d3d4d6;
    --field-2: #dfe0e2;
    --field-3: #eaebec;
    --text-dark: #222222;
  }
  * { box-sizing: border-box; margin: 0; padding: 0; }
  html, body {
    width: 1200px; height: 800px; overflow: hidden;
    background: var(--backdrop);
    font-family: "Lato", Arial, sans-serif;
  }
  .sheet {
    width: 1200px; height: 800px;
    display: flex; align-items: center; justify-content: center; gap: 44px;
  }
  .card {
    position: relative;
    width: 540px; height: 309px;
    background: var(--card-white);
    overflow: hidden;
    box-shadow: 0 6px 18px rgba(0,0,0,.35);
  }

  /* Brand name */
  .brand {
    position: absolute;
    display: flex; align-items: center; gap: 8px;
    color: var(--brand-red);
    font-weight: 900; font-size: 21px; letter-spacing: -.2px;
    white-space: nowrap;
  }
  .brand-dot {
    width: 13px; height: 13px; border-radius: 50%;
    background: var(--sky-blue);
  }

  /* Front side */
  .front-panel {
    position: absolute; left: 0; top: 0; width: 100%; height: 86%;
    background: var(--panel-mist);
  }
  .front .brand { right: 24px; top: 34px; }
  .contact-row {
    position: absolute; height: 24px;
    display: flex; align-items: center;
    color: #fff; font-size: 13px; padding-left: 12px;
  }
  .row-phone { left: 56%; right: 0; top: 92px; background: var(--ink-black); }
  .row-web   { left: 57%; right: 0; top: 118px; background: var(--steel-gray); }
  .row-mail  { left: 57%; right: 0; top: 144px; background: var(--ash-gray); }
  .icon-cell {
    position: absolute; left: 40%; width: 16.6%; height: 24px;
    display: flex; align-items: center; justify-content: center;
  }
  .icon-phone { top: 118px; background: var(--sky-blue); }
  .icon-link  { top: 144px; background: var(--sky-light); }
  .icon-mail  { top: 170px; background: var(--sky-pale); }
  .icon-cell svg { width: 14px; height: 14px; }

  .name-block {
    position: absolute; left: 22%; top: 178px; width: 28%; height: 88px;
    background: var(--brand-red); color: #fff;
    padding: 24px 0 0 20px;
  }
  .name-block .person { font-weight: 700; font-size: 20px; line-height: 1.1; }
  .name-block .role { font-size: 13px; margin-top: 2px; }
  .accent-block {
    position: absolute; left: 12%; top: 198px; width: 9%; height: 68px;
    background: var(--brand-red);
  }

  /* Back side */
  .appointment {
    position: absolute; left: 120px; top: 104px;
    display: grid; grid-template-columns: 100px 160px; grid-auto-rows: 22px; gap: 2px;
    font-size: 12px; color: var(--text-dark);
  }
  .appointment .label { display: flex; align-items: center; padding-left: 12px; }
  .label-appointment { background: var(--sky-blue); }
  .label-time { background: var(--sky-light); }
  .label-date { background: var(--sky-pale); }
  .field-1 { background: var(--field-1); }
  .field-2 { background: var(--field-2); }
  .field-3 { background: var(--field-3); }
  .back .brand { right: 22px; top: 200px; }
</style>
</head>
<body>
<main class="sheet">
  <section class="card front" aria-label="Business card front">
    <div class="front-panel"></div>
    <div class="brand"><span>Brightpath Weightloss</span><span class="brand-dot"></span></div>

    <div class="contact-row row-phone">555 014 268</div>
    <div class="contact-row row-web">www.brightpathsite.com</div>
    <div class="contact-row row-mail">samcarter@mailbox.com</div>

    <div class="icon-cell icon-phone">
      <svg viewBox="0 0 24 24" fill="#fff"><path d="M6.6 10.8a15.1 15.1 0 0 0 6.6 6.6l2.2-2.2c.3-.3.7-.4 1-.2 1.1.4 2.3.6 3.6.6.6 0 1 .4 1 1V20c0 .6-.4 1-1 1A17 17 0 0 1 3 4c0-.6.4-1 1-1h3.5c.6 0 1 .4 1 1 0 1.3.2 2.5.6 3.6.1.3 0 .7-.2 1z"/></svg>
    </div>
    <div class="icon-cell icon-link">
      <svg viewBox="0 0 24 24" fill="none" stroke="#fff" stroke-width="2.4" stroke-linecap="round"><path d="M10 14a4 4 0 0 0 5.7 0l3-3a4 4 0 0 0-5.7-5.7l-1 1"/><path d="M14 10a4 4 0 0 0-5.7 0l-3 3a4 4 0 0 0 5.7 5.7l1-1"/></svg>
    </div>
    <div class="icon-cell icon-mail">
      <svg viewBox="0 0 24 24" fill="#fff"><rect x="3" y="6" width="18" height="12" rx="1"/></svg>
    </div>

    <div class="accent-block"></div>
    <div class="name-block">
      <p class="person">Sam Carter</p>
      <p class="role">Manager</p>
    </div>
  </section>

  <section class="card back" aria-label="Business card back, appointment side">
    <div class="appointment">
      <div class="label label-appointment">Appointment</div><div class="field-1"></div>
      <div class="label label-time">Time</div><div class="field-2"></div>
      <div class="label label-date">Date</div><div class="field-3"></div>
    </div>
    <div class="brand"><span>Brightpath Weightloss</span><span class="brand-dot"></span></div>
  </section>
</main>
</body>
</html>
```